Fundraising Flyer for a School Library

We are a small but fast-growing school in need of funding support for a new Library, Admin and 2 more primary classrooms.
We are hoping that someone can come up with a design for a flyer (A4 - 3 fold) or brochure (2 to an A4) that will encourage people in our community to consider 'partnering' with us to help fund this massive project.
The 'Word' doc attached has some initial wording ideas, however someone with a gift for this type of advertising may well come up with better wording. We're happy for you to use a bit of creativity here.

Target Market(s)

Local businesses, parents and extended families

Industry/Entity Type

School

Requirements
Must have
• Picture of the proposed library.
• Pictures of students from our school.
• You can find information and photos on our school website. http://www.plrgs.example.edu.au/
Should not have
• Anything inappropriate for a Christian School.
• Pictures of random people that aren't from our school - ie, aren't in our school uniform.

```html
<!DOCTYPE html>
<html lang="en">
<head>
<meta charset="utf-8">
<title>Pine Lake Ridge CCS – Building Fund Brochure</title>
<link href="https://fonts.googleapis.com/css2?family=Open+Sans:wght@400;600;700&family=Oswald:wght@500;600;700&display=swap" rel="stylesheet">
<style>
  :root{
    --red:#d5251f;
    --red-dark:#b81c17;
    --navy:#2a2370;
    --white:#ffffff;
    --ink:#222222;
    --page:#e6e6e6;
    --grey-soft:#ececec;
  }
  *{box-sizing:border-box;margin:0;padding:0}
  html,body{width:1200px;height:1121px;overflow:hidden;background:var(--page)}
  body{font-family:"Open Sans",sans-serif;color:var(--ink);position:relative}
  .spread{position:absolute;left:215px;width:770px;height:548px;background:var(--white);overflow:hidden;box-shadow:0 2px 8px rgba(0,0,0,.25)}
  .spread--outside{top:8px}
  .spread--inside{top:565px}
  .abs{position:absolute}
  .shape{position:absolute;left:0;top:0}
  .photo{position:absolute}
  .panel{position:absolute;top:0;height:548px;overflow:hidden}
  .panel--1{left:0;width:257px}
  .panel--2{left:257px;width:256px}
  .panel--3{left:513px;width:257px}

  .crest{position:absolute;width:80px;height:80px;border-radius:50%;background:var(--white);display:flex;align-items:center;justify-content:center;text-align:center;font:700 11px/1.15 "Open Sans",sans-serif;color:var(--navy)}

  .school-name{position:absolute;left:0;width:100%;text-align:center;font-weight:600;font-size:22px;line-height:1}
  .school-sub{position:absolute;left:0;width:100%;text-align:center;font-weight:600;font-size:10.5px}

  /* about panel */
  .about-title{left:78px;top:12px;font:600 17px "Oswald",sans-serif;color:var(--white)}
  .about-copy{left:14px;top:112px;width:232px;font-size:7px;line-height:1.45;text-align:justify}
  .about-copy p{margin-bottom:7px}
  .about-copy h3{font:600 11px "Oswald",sans-serif;color:var(--red);margin:2px 0 4px}
  .about-copy ul{list-style:none}
  .about-copy li{position:relative;padding-left:10px;margin-bottom:6px;text-align:left}
  .about-copy li::before{content:"";position:absolute;left:0;top:3px;width:5px;height:5px;border-radius:50%;background:var(--navy)}
  .about-copy li b{display:block;font-size:7px;font-weight:700}

  /* contacts */
  .contacts{left:0;width:256px;top:448px;color:var(--white);font-size:7.2px;line-height:1.35;text-align:center}
  .contacts div{margin-bottom:5px}
  .contacts .ico{display:inline-block;width:7px;height:7px;margin-right:4px;vertical-align:-1px}

  /* cover */
  .cover-lead{left:0;width:257px;top:440px;text-align:center;color:var(--navy);font-weight:600;font-size:22px}
  .cover-goal{left:0;width:257px;top:466px;text-align:center;color:var(--red);font:600 22px/1.28 "Oswald",sans-serif;letter-spacing:.2px}

  /* inside: appeal */
  .appeal{left:0;width:257px;text-align:center;color:var(--white);white-space:nowrap}
  .appeal-1{top:22px;font-size:22px;font-weight:600}
  .appeal-2{top:53px;font-size:15px}
  .appeal-amount{top:74px;font:700 66px/1 "Oswald",sans-serif;letter-spacing:-1px}
  .appeal-more{top:152px;font:700 34px/1 "Oswald",sans-serif}
  .appeal-3{top:193px;font-size:16.5px;font-weight:600}
  .appeal-4{top:214px;font-size:13.5px}

  .details{left:270px;top:245px;width:500px;height:260px;font-size:9.4px;color:var(--ink)}
  .details-intro{position:absolute;left:0;top:0;width:260px;line-height:1.35}
  .row-label{position:absolute;left:2px;font:600 13px "Oswald",sans-serif;color:var(--red);letter-spacing:.3px}
  .row-item{position:absolute;font-size:9px;white-space:nowrap}
  .details-line{position:absolute;left:2px;font-size:9.6px;line-height:1.35}

  .progress{left:516px;top:419px;width:254px;height:129px;background:var(--navy);color:var(--white);padding:10px 8px 0 8px;font-size:8.6px;line-height:1.3}
  .progress h4{font:600 14px "Oswald",sans-serif;color:var(--red);margin-bottom:4px}
  .progress p{margin-bottom:8px}

  .web-strip{left:257px;top:511px;width:259px;height:37px;background:var(--red);color:var(--white);font-size:11.5px;letter-spacing:4px;text-align:center;line-height:37px}
</style>
</head>
<body>

<!-- ============ OUTSIDE SPREAD ============ -->
<section class="spread spread--outside">

  <!-- Panel 1: About School -->
  <div class="panel panel--1">
    <svg class="shape" width="257" height="548" viewBox="0 0 257 548">
      <path d="M0 0H257V50C170 44 80 60 0 88Z" fill="var(--red)"/>
      <path d="M0 92C70 66 170 52 257 56V64C170 62 80 78 0 106Z" fill="var(--navy)"/>
    </svg>
    <div class="abs about-title">About School</div>
    <div class="abs about-copy">
      <p>The Pine Lake Ridge Christian Community School provides an education with a difference. We are a family based school with a Christ centred ethos and heritage.</p>
      <p>Our teachers are committed to every student. The school delivers Christian values and quality education; is personal and professional and trains students to respect others and be accountable in their learning and behaviour towards others.</p>
      <p>We encourage you to find out what our school has to offer for your family. Please contact our school office and we can organise a tour of the school so that you can see our school in action.</p>
      <h3>STUDENTS CAN....</h3>
      <ul>
        <li><b>BE THEMSELVES</b>PLRCS is a place where students can BE THEMSELVES with confidence and without fear.</li>
        <li><b>BELONG</b>PLRCS students can belong to a community and make a contribution.</li>
        <li><b>BELIEVE</b>In the Lordship of Jesus Christ, understand His grace and their responsibilities to Him.</li>
        <li><b>BEHAVE</b>PLRCS teaches students to behave in a way that prepares each student to be a citizen in our wider society.</li>
      </ul>
    </div>
    <div class="photo" role="img" aria-label="Photo of students and a teacher gathered around a laptop and 3D printer" style="left:0;top:402px;width:257px;height:146px;background:linear-gradient(160deg,#d9dde3 0%,#9fb4cc 40%,#3c5f9c 75%,#b89a78 100%)"></div>
  </div>

  <!-- Panel 2: Back -->
  <div class="panel panel--2">
    <div class="photo" role="img" aria-label="Faded photo of a classroom interior" style="left:0;top:0;width:256px;height:548px;background:linear-gradient(180deg,#f2f2f2 0%,#e2e2e2 40%,#d6d6d6 70%,#eeeeee 100%)"></div>
    <svg class="shape" width="256" height="548" viewBox="0 0 256 548">
      <path d="M256 62C170 64 90 110 56 180C98 120 170 92 256 86Z" fill="var(--navy)"/>
      <path d="M0 418C90 446 170 420 256 392V548H0Z" fill="var(--red)"/>
      <path d="M0 426C90 452 170 426 256 399V548H0Z" fill="var(--white)"/>
      <path d="M0 430C90 456 170 432 256 406V548H0Z" fill="var(--navy)"/>
      <path d="M140 548C200 540 235 525 256 505V548Z" fill="var(--white)"/>
    </svg>
    <div class="crest" style="left:88px;top:225px;border:3px solid var(--navy)">Pine Lake<br>Ridge</div>
    <div class="school-name" style="top:316px;color:var(--navy)">Pine Lake Ridge</div>
    <div class="school-sub" style="top:337px;color:var(--navy)">Christian Community School</div>
    <div class="abs contacts">
      <div><svg class="ico" viewBox="0 0 10 10"><path d="M2 0L4 2.5 3 4C3.8 5.6 4.6 6.4 6 7L7.5 6 10 8 8.5 10C4 9.5.5 6 0 1.5Z" fill="var(--red)"/></svg>02 5550 1234</div>
      <div><svg class="ico" viewBox="0 0 10 8"><rect width="10" height="8" fill="var(--red)"/><path d="M0 0L5 4.5 10 0" stroke="var(--white)" fill="none"/></svg>office@plrgs.example.edu.au</div>
      <div><svg class="ico" viewBox="0 0 10 10"><circle cx="5" cy="5" r="4.3" stroke="var(--red)" stroke-width="1.2" fill="none"/><path d="M1 5H9M5 1C3 3.5 3 6.5 5 9M5 1C7 3.5 7 6.5 5 9" stroke="var(--red)" stroke-width=".8" fill="none"/></svg>www.partners.example.org</div>
      <div><svg class="ico" viewBox="0 0 8 10"><path d="M4 0C1.8 0 0 1.8 0 4C0 6.5 4 10 4 10S8 6.5 8 4C8 1.8 6.2 0 4 0Z" fill="var(--red)"/><circle cx="4" cy="4" r="1.5" fill="var(--navy)"/></svg>PO Box 48 Harbour Road<br>Pine Lake<br>NSW 2999<br>Australia</div>
    </div>
  </div>

  <!-- Panel 3: Front cover -->
  <div class="panel panel--3">
    <div class="photo" role="img" aria-label="Architectural rendering of the proposed new library building" style="left:0;top:150px;width:257px;height:260px;background:linear-gradient(180deg,#f4f4f4 0%,#cfc9c4 40%,#8c7d74 58%,#c8c2cc 78%,#7f9c58 100%)"></div>
    <svg class="shape" width="257" height="548" viewBox="0 0 257 548">
      <path d="M0 0H257V138C170 160 90 150 0 140Z" fill="var(--red)"/>
      <path d="M0 146C90 156 170 166 257 144V176C170 196 90 170 0 164Z" fill="var(--navy)"/>
      <path d="M0 160C90 168 170 180 257 152V150C170 172 90 162 0 152Z" fill="var(--white)"/>
      <path d="M0 380C70 390 140 370 200 372C230 374 245 385 257 392V548H0Z" fill="var(--navy)"/>
      <path d="M0 402C70 382 150 384 257 404V548H0Z" fill="var(--red)"/>
      <path d="M0 410C70 390 150 392 257 412V548H0Z" fill="var(--white)"/>
    </svg>
    <div class="crest" style="left:88px;top:10px">Pine Lake<br>Ridge</div>
    <div class="school-name" style="top:94px;color:var(--white)">Pine Lake Ridge</div>
    <div class="school-sub" style="top:117px;color:var(--white)">Christian Community School</div>
    <div class="abs cover-lead">Fundraising for</div>
    <div class="abs cover-goal">New Library, Office and<br>2 Primary Class Rooms</div>
  </div>
</section>

<!-- ============ INSIDE SPREAD ============ -->
<section class="spread spread--inside">

  <!-- Appeal panel -->
  <div class="panel panel--1">
    <div class="photo" role="img" aria-label="Photo of two students in school uniform with a staff member beside a display table" style="left:0;top:250px;width:257px;height:298px;background:linear-gradient(180deg,#d8d2c6 0%,#b9c6d4 35%,#9cc3df 60%,#6b4a2e 100%)"></div>
    <svg class="shape" width="257" height="548" viewBox="0 0 257 548">
      <path d="M0 0H257V244C170 244 80 258 0 282Z" fill="var(--red)"/>
      <path d="M0 282C80 258 170 244 257 244V254C170 254 80 266 0 290Z" fill="var(--white)"/>
    </svg>
    <div class="abs appeal appeal-1">100 Partners sought</div>
    <div class="abs appeal appeal-2">To raise</div>
    <div class="abs appeal appeal-amount">$50,000</div>
    <div class="abs appeal appeal-more">or more</div>
    <div class="abs appeal appeal-3">By Tax deductable donations</div>
    <div class="abs appeal appeal-4">to the PLRCS building fund</div>
  </div>

  <!-- Ceremony photo across two panels -->
  <div class="photo" role="img" aria-label="Photo of school representatives cutting a red ribbon at an opening ceremony" style="left:257px;top:0;width:513px;height:250px;background:linear-gradient(180deg,#c9d6e2 0%,#90a8bf 35%,#3e4b72 70%,#6f8a5c 100%)"></div>
  <svg class="shape" width="770" height="548" viewBox="0 0 770 548">
    <path d="M257 210C350 180 440 200 520 228C600 252 680 256 770 232V548H257Z" fill="var(--navy)"/>
    <path d="M257 222C350 192 440 212 520 240C600 262 680 264 770 246V548H257Z" fill="var(--red)"/>
    <path d="M257 228C350 200 440 220 520 248C600 270 680 272 770 256V548H257Z" fill="var(--white)"/>
    <path d="M257 232C350 206 440 226 520 254C600 276 680 278 770 262V548H257Z" fill="var(--grey-soft)"/>
    <path d="M257 250C400 270 600 300 770 290V548H257Z" fill="var(--white)"/>
  </svg>

  <div class="abs details">
    <p class="details-intro">Towards the cost of the constructing the new Library, Offices and providing 2 additional Primary Class Rooms. The total cost is $1.45m.</p>
    <div class="row-label" style="top:47px">WHO</div>
    <div class="row-item" style="left:87px;top:49px">School families</div>
    <div class="row-item" style="left:182px;top:49px">Grandparents</div>
    <div class="row-item" style="left:290px;top:49px">Church members</div>
    <div class="row-item" style="left:405px;top:49px">Christian Community</div>
    <div class="row-item" style="left:87px;top:63px">Local Pine Lake Businesses</div>
    <div class="row-item" style="left:222px;top:63px">Others</div>

    <div class="row-label" style="top:94px">WHEN</div>
    <div class="row-item" style="left:88px;top:96px">By 30 June 2016</div>

    <div class="row-label" style="top:127px">HOW MUCH</div>
    <div class="row-item" style="left:87px;top:129px">$100</div>
    <div class="row-item" style="left:138px;top:129px">$200</div>
    <div class="row-item" style="left:186px;top:129px">$500</div>
    <div class="row-item" style="left:245px;top:129px">$1000</div>
    <div class="row-item" style="left:303px;top:129px">$2000</div>
    <div class="row-item" style="left:356px;top:129px">$5000</div>
    <div class="row-item" style="left:419px;top:129px">Other</div>

    <div class="row-label" style="top:153px">WHERE</div>
    <div class="row-item" style="left:86px;top:155px">Donate:</div>

    <div class="details-line" style="top:179px">through the School office directly</div>
    <div class="details-line" style="top:202px">or.... By cheque to; PLRCS,&nbsp;&nbsp; PO Box 48,<br>Pine Lake, NSW, 2999&nbsp; by</div>
    <div class="details-line" style="top:236px">or....direct deposit A/C-------------</div>
  </div>

  <div class="abs web-strip">www.partners.example.org</div>

  <div class="abs progress">
    <h4>PROGRESS REPORTS</h4>
    <p><b>Number of Partners</b> and progress on <b>money raised</b> will be included in ‘<b>The Messenger</b>’ each week during second term. Individual names will be kept confidential.</p>
    <p>Business Names will be listed in the end of term Messenger and on the School WEB site.</p>
  </div>
</section>

</body>
</html>
```